Branding Pack for new business to business cost saving site

I would like a branding pack for my new project. I would like the following designed;
a4 Presentation folder
Letterhead
Envelope
Business Card
compliment splip

We are a business cost saving site, we have access to 1000s of discount offers for daily business to business offers. I already have the logo therfore please follow th e logo for the coloutr and design.

Target Market(s)

SMEs in United Kingdom

Industry/Entity Type

Business Service

Font styles to use
Serif
Script

Colors
0255a3
fbee3d

Requirements
Must have
• The folder needs to be the same size as attached

```html
<!DOCTYPE html>
<html lang="en">
<head>
<meta charset="utf-8">
<title>Thriftly Stationery Pack</title>
<link rel="stylesheet" href="https://fonts.googleapis.com/css2?family=Montserrat:wght@400;500;700;800&family=Noto+Serif:wght@400;700&display=swap">
<style>
:root{
  --navy:#2f3a7c;
  --yellow:#fdd544;
  --paper:#ffffff;
  --paper-soft:#f4f5f4;
  --backdrop:#ddd3c1;
  --ink:#2f3a7c;
  --shadow:0 6px 10px rgba(60,45,20,.22);
}
*{box-sizing:border-box;margin:0;padding:0}
html,body{width:1200px;height:1200px;overflow:hidden}
body{background:var(--backdrop);position:relative;font-family:"Noto Serif",serif;color:var(--ink)}
.piece{position:absolute;overflow:hidden;box-shadow:var(--shadow);background:var(--paper)}
.brand{display:inline-flex;align-items:flex-start;gap:2px;line-height:1}
.brand-name{font-family:"Montserrat",sans-serif;font-weight:500;color:var(--navy);letter-spacing:-.02em}
.brand-dot{border-radius:50%;background:var(--yellow);flex:none}
.brand.on-navy .brand-name{color:#fff}
.accent-circle{position:absolute;border-radius:50%;background:var(--yellow)}
.icon{width:6px;height:6px;display:inline-block;vertical-align:middle}

/* Letterhead */
.letterhead{left:137px;top:147px;width:287px;height:406px}
.letterhead .brand{position:absolute;left:41px;top:40px}
.letterhead .address{position:absolute;left:44px;top:66px;font-size:5.4px}
.letterhead .salutation{position:absolute;left:42px;top:98px;font-size:4.5px;line-height:1.35}
.letterhead .salutation b{font-size:5px}
.letterhead .date{position:absolute;right:41px;top:108px;font-family:"Montserrat",sans-serif;font-weight:700;font-size:5px}
.letterhead .body{position:absolute;left:42px;top:128px;width:204px;font-size:4.8px;line-height:1.4;text-align:justify}
.letterhead .body p{margin-bottom:7px}
.letterhead .sign{position:absolute;right:41px;top:330px;text-align:right;font-size:4px}
.letterhead .sign .line{width:40px;border-top:.6px solid var(--navy);margin:0 0 6px auto}
.letterhead .sign b{font-family:"Montserrat",sans-serif;font-size:5.4px;display:block}
.letterhead .footer{position:absolute;left:68px;top:382px;display:flex;gap:16px;font-size:3.4px;align-items:center}
.letterhead .footer span{display:flex;align-items:center;gap:4px}
.letterhead .band{position:absolute;left:0;bottom:0;width:100%;height:8px;background:var(--navy)}
.letterhead .band-accent{position:absolute;right:0;bottom:0;width:72px;height:8px;background:var(--yellow);clip-path:polygon(22% 0,100% 0,100% 100%,0 100%)}

/* Business card */
.card-front{left:409px;top:224px;width:214px;height:122px;background:var(--navy)}
.card-front .brand{position:absolute;left:54px;top:52px}
.card-back{left:413px;top:365px;width:210px;height:122px}
.card-back .brand{position:absolute;left:16px;top:24px}
.card-back .contact{position:absolute;left:17px;top:62px;font-size:4.6px;line-height:2.45}
.card-back .contact .row{display:flex;align-items:center;gap:6px}
.card-back .contact .bullet{width:5px;height:5px;border-radius:50%;background:var(--navy)}
.card-back .person{position:absolute;right:21px;top:91px;text-align:right;font-size:5px}
.card-back .person b{font-family:"Montserrat",sans-serif;font-size:6px;display:block}

/* Envelope */
.envelope-back{left:681px;top:209px;width:346px;height:174px;background:var(--paper-soft)}
.envelope-back .flap{position:absolute;left:0;top:0;width:100%;height:58px;background:var(--navy);clip-path:polygon(0 0,100% 0,98% 88%,96.5% 100%,3.5% 100%,2% 88%);overflow:hidden}
.envelope-front{left:742px;top:370px;width:346px;height:173px;background:var(--paper-soft)}
.envelope-front .brand{position:absolute;right:20px;top:27px}
.envelope-front .window{position:absolute;left:26px;top:66px;width:118px;height:59px;border-radius:9px;background:linear-gradient(120deg,#2f3a7c 0%,#3d4a95 55%,#2f3a7c 100%);box-shadow:-2px 2px 2px rgba(0,0,0,.25)}
.envelope-front .contact{position:absolute;right:19px;top:117px;text-align:right;font-size:6.6px;line-height:1.35}

/* Folder */
.folder-side{position:absolute;left:110px;top:620px;width:56px;height:389px;background:var(--paper);clip-path:polygon(100% 0,100% 100%,0 86%,0 7%);box-shadow:var(--shadow)}
.folder-bottom{position:absolute;left:166px;top:1009px;width:282px;height:66px;background:var(--paper);clip-path:polygon(0 0,100% 0,100% 22%,76% 100%,0 100%)}
.folder-cover{left:166px;top:620px;width:282px;height:389px;background:var(--navy);box-shadow:none}
.folder-cover .footer{position:absolute;left:69px;top:366px;display:flex;gap:14px;font-size:3.4px;color:#fff;align-items:center}
.folder-cover .footer span{display:flex;align-items:center;gap:4px}
.folder-inside{left:448px;top:620px;width:284px;height:389px;background:repeating-linear-gradient(135deg,#fff 0 3px,#f7f7f7 3px 4px);box-shadow:none}
.folder-inside .brand{position:absolute;left:62px;top:172px}

/* Compliment slip */
.slip{left:709px;top:659px;width:369px;height:173px;background:var(--paper-soft)}
.slip .brand{position:absolute;left:29px;top:30px}
.slip .contact{position:absolute;left:29px;top:102px;font-size:6.5px;line-height:1.45}
.slip .ribbon{position:absolute;left:0;top:138px;width:180px;height:24px;background:var(--navy);clip-path:polygon(0 0,86% 0,100% 100%,0 100%);color:#fff;font-family:"Montserrat",sans-serif;font-weight:800;font-size:8px;letter-spacing:.08em;display:flex;align-items:center;padding-left:30px}
</style>
</head>
<body>

<!-- Letterhead -->
<section class="piece letterhead" aria-label="Letterhead">
  <div class="accent-circle" style="left:200px;top:-48px;width:110px;height:110px"></div>
  <div class="brand"><span class="brand-name" style="font-size:17px">thriftly</span><span class="brand-dot" style="width:4px;height:4px"></span></div>
  <p class="address">48 Harbour Row, Leeds LS2 7QT</p>
  <div class="salutation"><b>Dear, Mr.________</b><br>Designation<br>COMPANY NAME</div>
  <p class="date">DATE:1/5/2018</p>
  <div class="body">
    <p>Our team reviews supplier costs every month and brings members exclusive savings on energy, telecoms, stationery, travel, insurance and office supplies. Each offer is checked for value and clear terms, so small firms can switch with confidence and keep more of their budget for growth and hiring. We also track renewal dates, compare new tariffs as they appear and alert you early, so no contract rolls over at a higher price without notice.</p>
    <p>Our team reviews supplier costs every month and brings members exclusive savings on energy, telecoms, stationery, travel, insurance and office supplies. Each offer is checked for value and clear terms, so small firms can switch with confidence and keep more of their budget for growth and hiring. We also track renewal dates, compare new tariffs as they appear and alert you early, so no contract rolls over at a higher price without notice.</p>
    <p>Our team reviews supplier costs every month and brings members exclusive savings on energy, telecoms, stationery, travel, insurance and office supplies. Each offer is checked for value and clear terms, so small firms can switch with confidence and keep more of their budget for growth and hiring. We also track renewal dates, compare new tariffs as they appear and alert you early, so no contract rolls over at a higher price without notice.</p>
    <p>Our team reviews supplier costs every month and brings members exclusive savings on energy, telecoms, stationery, travel, insurance and office supplies. Each offer is checked for value and clear terms, so small firms can switch with confidence and keep more of their budget for growth and hiring. We also track renewal dates, compare new tariffs as they appear and alert you early, so no contract rolls over at a higher price without notice.</p>
  </div>
  <div class="sign"><div class="line"></div><b>YOUR NAME</b>Designation</div>
  <div class="footer">
    <span><svg class="icon" viewBox="0 0 10 10"><path d="M2 1l2 0 1 2.5-1.3 1a5 5 0 0 0 2.8 2.8l1-1.3L10 7v2a1 1 0 0 1-1 1A9 9 0 0 1 0 1a1 1 0 0 1 1-1z" fill="currentColor"/></svg>00-987-654-321</span>
    <span><svg class="icon" viewBox="0 0 10 10"><rect x="0" y="2" width="10" height="6" fill="currentColor"/><path d="M0 2l5 3.5L10 2" stroke="#fff" fill="none"/></svg>hello@thriftly.co</span>
    <span><svg class="icon" viewBox="0 0 10 10"><circle cx="5" cy="5" r="4.4" fill="none" stroke="currentColor"/><path d="M0.6 5h8.8M5 .6c-2.5 2.5-2.5 6.3 0 8.8M5 .6c2.5 2.5 2.5 6.3 0 8.8" fill="none" stroke="currentColor" stroke-width=".7"/></svg>www.thriftly.co</span>
  </div>
  <div class="band"></div>
  <div class="band-accent"></div>
</section>

<!-- Business card front -->
<section class="piece card-front" aria-label="Business card front">
  <div class="brand on-navy"><span class="brand-name" style="font-size:20px">thriftly</span><span class="brand-dot" style="width:5px;height:5px"></span></div>
</section>

<!-- Business card back -->
<section class="piece card-back" aria-label="Business card back">
  <div class="accent-circle" style="left:120px;top:10px;width:50px;height:50px"></div>
  <div class="brand"><span class="brand-name" style="font-size:13px">thriftly</span><span class="brand-dot" style="width:3px;height:3px"></span></div>
  <div class="contact">
    <div class="row"><span class="bullet"></span>00-987-654-321</div>
    <div class="row"><span class="bullet"></span>hello@thriftly.co</div>
    <div class="row"><span class="bullet"></span>www.thriftly.co</div>
    <div class="row"><span class="bullet"></span>48 Harbour Row, Leeds LS2 7QT</div>
  </div>
  <div class="person"><b>ALEX REED</b>Director</div>
</section>

<!-- Envelope back -->
<section class="piece envelope-back" aria-label="Envelope back">
  <div class="flap">
    <div class="accent-circle" style="left:241px;top:9px;width:52px;height:52px"></div>
  </div>
</section>

<!-- Envelope front -->
<section class="piece envelope-front" aria-label="Envelope front">
  <div class="brand"><span class="brand-name" style="font-size:21px">thriftly</span><span class="brand-dot" style="width:5px;height:5px"></span></div>
  <div class="window"></div>
  <div class="contact">00-987-654-321<br>hello@thriftly.co<br>www.thriftly.co<br>48 Harbour Row, Leeds LS2 7QT</div>
</section>

<!-- Presentation folder -->
<div class="folder-side"></div>
<div class="folder-bottom"></div>
<section class="piece folder-cover" aria-label="Presentation folder cover">
  <div class="accent-circle" style="left:61px;top:37px;width:114px;height:114px"></div>
  <div class="footer">
    <span><svg class="icon" viewBox="0 0 10 10"><path d="M2 1l2 0 1 2.5-1.3 1a5 5 0 0 0 2.8 2.8l1-1.3L10 7v2a1 1 0 0 1-1 1A9 9 0 0 1 0 1a1 1 0 0 1 1-1z" fill="currentColor"/></svg>00-987-654-321</span>
    <span><svg class="icon" viewBox="0 0 10 10"><rect x="0" y="2" width="10" height="6" fill="currentColor"/><path d="M0 2l5 3.5L10 2" stroke="#2f3a7c" fill="none"/></svg>hello@thriftly.co</span>
    <span><svg class="icon" viewBox="0 0 10 10"><circle cx="5" cy="5" r="4.4" fill="none" stroke="currentColor"/><path d="M0.6 5h8.8M5 .6c-2.5 2.5-2.5 6.3 0 8.8M5 .6c2.5 2.5 2.5 6.3 0 8.8" fill="none" stroke="currentColor" stroke-width=".7"/></svg>www.thriftly.co</span>
  </div>
</section>
<section class="piece folder-inside" aria-label="Presentation folder back panel">
  <div class="brand"><span class="brand-name" style="font-size:33px">thriftly</span><span class="brand-dot" style="width:7px;height:7px"></span></div>
</section>

<!-- Compliment slip -->
<section class="piece slip" aria-label="Compliment slip">
  <div class="accent-circle" style="left:240px;top:85px;width:64px;height:64px"></div>
  <div class="brand"><span class="brand-name" style="font-size:20px">thriftly</span><span class="brand-dot" style="width:5px;height:5px"></span></div>
  <div class="contact">00-987-654-321<br>hello@thriftly.co<br>www.thriftly.co<br>48 Harbour Row, Leeds LS2 7QT</div>
  <div class="ribbon">WITH COMPLIMENTS</div>
</section>

</body>
</html>
```